Redesign Local Plumber Website

redesign of existing plumbing website

Mobile Responsive
Professional
modern
easy enquiry
Map embed

Please see existing site for text and images. Please feel free to suggest improvements and any additional features
callmeforyourpipes.com.au

attached is logo and the Australian owned badge which we also want featuring

Target Market(s)

Plumbing & Gas Services

Industry/Entity Type

Plumbing

Font styles to use
Sans Serif

Requirements
Must have
• existing logo
Nice to have
• new design
Should not have
• same design

```html
<!DOCTYPE html>
<html lang="en">
<head>
<meta charset="utf-8">
<title>Call Me For Your Pipes – Plumbing &amp; Gas</title>
<link rel="stylesheet" href="https://fonts.googleapis.com/css2?family=Raleway:wght@700;800;900&family=Lato:wght@400;700;900&display=swap">
<style>
:root{
  --navy:#14105a;
  --navy-deep:#0f0c47;
  --blue:#1592d3;
  --blue-dark:#0f78b4;
  --ink:#111;
  --text:#6a6a6a;
  --light:#f1f1f3;
  --footer:#3b3b3e;
  --white:#fff;
}
*{box-sizing:border-box;margin:0;padding:0}
html,body{width:1200px;height:4677px;overflow:hidden}
body{position:relative;background:var(--white);font-family:'Lato',sans-serif;color:var(--text)}
.abs{position:absolute}
.heading{font-family:'Raleway',sans-serif;font-weight:800;color:var(--ink);letter-spacing:1px}
.btn{position:absolute;background:var(--blue);color:var(--white);font-family:'Lato',sans-serif;font-weight:900;font-size:14px;display:flex;align-items:center;justify-content:center;gap:10px;text-transform:uppercase;box-shadow:0 0 0 3px rgba(21,146,211,.15)}
.btn .arrow{width:14px;height:14px;border-radius:50%;background:var(--white);position:relative}
.btn .arrow::after{content:"";position:absolute;left:4px;top:4px;border:3px solid transparent;border-left:5px solid var(--blue)}

.topbar{left:0;top:0;width:1200px;height:85px;background:var(--white)}
.navbar{left:0;top:85px;width:1200px;height:48px;background:var(--navy)}
.nav a{position:absolute;top:102px;color:var(--white);font-weight:900;font-size:14px;text-decoration:none}
.logo-box{left:109px;top:0;width:187px;height:142px;background:var(--white);border-radius:0 0 6px 6px;box-shadow:0 2px 6px rgba(0,0,0,.25);display:flex;align-items:center;justify-content:center;text-align:center;padding:0 12px}
.logo-name{font-family:'Raleway',sans-serif;font-weight:900;color:var(--navy);font-size:20px;line-height:1.15}
.showroom{left:378px;top:35px;font-weight:900;font-size:14px;color:var(--ink);display:flex;gap:10px;align-items:center}
.badge{left:630px;top:14px;width:60px;height:60px;border-radius:50%;background:#3f8f3c;border:4px solid #d9e9d2}
.tagline{left:714px;top:24px;font-style:italic;font-size:13px;line-height:21px;color:#555}
.freecall{left:875px;top:0;width:325px;height:133px;background:var(--blue);clip-path:polygon(70px 0,100% 0,100% 100%,0 100%)}
.freecall-label{left:1004px;top:43px;color:var(--white);font-weight:900;font-size:15px}
.freecall-num{left:928px;top:70px;color:var(--white);font-weight:700;font-size:26px}
.phone-ring{left:950px;top:34px;width:34px;height:34px;border-radius:50%;background:var(--navy)}

.hero{left:0;top:133px;width:1200px;height:562px;background:linear-gradient(90deg,#1c1d22 0%,#34363d 55%,#22242a 100%)}
.hero-person{left:762px;top:133px;width:254px;height:562px;background:linear-gradient(180deg,#6d5a3e 0%,#4f6f9e 35%,#3c5a86 70%,#5a4a34 100%);border-radius:100px 100px 0 0;opacity:.85}
.hero-title{left:111px;top:270px;color:var(--white);font-family:'Raleway',sans-serif;font-weight:900;font-size:64px;line-height:66px;letter-spacing:1px}
.hero-text{left:111px;top:424px;width:550px;color:var(--white);font-size:13.5px;line-height:25px}
.hero-text span{color:var(--blue)}

.enquiry{left:0;top:695px;width:1200px;height:171px;background:var(--navy-deep)}
.enquiry-title{left:111px;top:731px;color:var(--white);font-weight:900;font-size:16px;letter-spacing:.5px}
.field{position:absolute;top:777px;height:44px;background:var(--white);font-size:12px;color:#777;padding:14px 12px}
.callbox{left:848px;top:686px;width:279px;height:160px;background:var(--blue);clip-path:polygon(0 0,100% 0,100% 105px,50% 160px,0 105px)}
.callbox-label{left:848px;top:703px;width:279px;text-align:center;color:var(--navy-deep);font-weight:900;font-size:21px;letter-spacing:1px}
.callbox-num{left:848px;top:737px;width:279px;text-align:center;color:var(--white);font-weight:900;font-size:31px;letter-spacing:1px}

.splash{left:0;top:1150px;width:540px;height:317px;background:radial-gradient(ellipse at 45% 60%,#7fc1e6 0%,#c6e3f4 40%,rgba(255,255,255,0) 72%)}
.feature-icon{position:absolute;left:108px;width:62px;height:62px;border-radius:50%;background:var(--white);border:2px solid #dfe6ef;border-bottom:3px solid var(--navy);display:flex;align-items:center;justify-content:center}
.feature-title{position:absolute;left:203px;font-weight:900;font-size:13px;color:var(--ink)}
.feature-text{position:absolute;left:203px;width:330px;font-size:13.5px;line-height:24px;color:var(--text)}
.about-title{left:621px;top:950px;font-size:30px}
.about-text{left:621px;width:455px;font-size:13.5px;line-height:25.5px}

.partners{left:0;top:1467px;width:1200px;height:203px;background:var(--light)}
.partner{position:absolute;top:1555px;height:38px;border-radius:19px;background:#d6d8de}

.section-title{left:0;width:1200px;text-align:center;font-size:30px}
.service-title{font-size:30px}
.checklist{list-style:none}
.checklist li{position:absolute;font-size:13.5px;color:#555;display:flex;align-items:center;gap:18px;white-space:nowrap}
.checklist li::before{content:"";width:11px;height:11px;border-radius:50%;border:2px solid var(--blue);box-sizing:border-box;flex:none}
.photo{position:absolute;box-shadow:0 0 0 6px #fff,0 3px 12px rgba(0,0,0,.18)}

.provide{left:0;top:2800px;width:1200px;height:612px;background:linear-gradient(180deg,#eceef2 0%,#f6f7f9 100%)}
.diamond{position:absolute;width:160px;height:160px;transform:rotate(45deg);background:var(--white);border-top:6px solid var(--blue);border-left:6px solid var(--blue);border-radius:12px;box-shadow:0 4px 14px rgba(0,0,0,.12)}
.diamond-label{position:absolute;width:240px;text-align:center;font-family:'Raleway',sans-serif;font-weight:800;font-size:15.5px;color:var(--ink);letter-spacing:.5px}
.diamond-icon{position:absolute;width:44px;height:44px}

.info-text{left:155px;top:3583px;width:890px;text-align:center;font-size:13.5px;line-height:29px;color:#555}

.map{left:0;top:3993px;width:1200px;height:387px;background:linear-gradient(135deg,#e6e6e6 0%,#dedede 60%,#cfe1c8 85%,#c4dcbc 100%)}
.directions{left:111px;top:4038px;width:210px;height:46px;background:var(--white);box-shadow:0 1px 4px rgba(0,0,0,.25);font-weight:700;font-size:13px;color:var(--ink);display:flex;align-items:center;justify-content:space-between;padding:0 20px}
.addr{left:394px;top:4220px;width:167px;height:85px;background:var(--white);box-shadow:0 1px 4px rgba(0,0,0,.25);text-align:center;font-size:11px;line-height:18px;color:#333;padding-top:12px}
.addr b{font-size:10px}

.footer{left:0;top:4380px;width:1200px;height:297px;background:var(--footer)}
.f-icon{position:absolute;width:42px;height:42px;border-radius:50%;border:2px solid var(--white);display:flex;align-items:center;justify-content:center}
.f-label{position:absolute;color:var(--white);font-weight:900;font-size:14px}
.f-value{position:absolute;color:var(--white);font-size:14px}
.f-logo{left:540px;top:4452px;width:220px;text-align:center;color:var(--white);font-family:'Raleway',sans-serif;font-weight:900;font-size:22px;line-height:1.1}
.f-nav{left:0;top:4553px;width:1200px;display:flex;justify-content:center;gap:16px;color:var(--white);font-weight:900;font-size:14px}
.f-nav span.sep{font-weight:400}
.f-rule{left:111px;top:4610px;width:978px;height:1px;background:#6b6b6f}
.f-copy{left:111px;top:4635px;color:var(--white);font-size:13px}
.f-legal{left:880px;top:4637px;color:var(--white);font-size:12px}
</style>
</head>
<body>

<div class="abs topbar"></div>
<div class="abs navbar"></div>
<div class="abs freecall"></div>
<div class="abs phone-ring"></div>
<svg class="abs" style="left:958px;top:42px" width="18" height="18" viewBox="0 0 24 24"><path fill="#fff" d="M6.6 10.8a15 15 0 0 0 6.6 6.6l2.2-2.2a1 1 0 0 1 1-.25 11.4 11.4 0 0 0 3.6.57 1 1 0 0 1 1 1V20a1 1 0 0 1-1 1A17 17 0 0 1 3 4a1 1 0 0 1 1-1h3.5a1 1 0 0 1 1 1c0 1.25.2 2.45.57 3.57a1 1 0 0 1-.25 1z"/></svg>
<div class="abs freecall-label">FREE CALL !</div>
<div class="abs freecall-num">1800 555 019</div>
<svg class="abs" style="left:1110px;top:28px;opacity:.3" width="70" height="70" viewBox="0 0 24 24"><path fill="#fff" d="M6.6 10.8a15 15 0 0 0 6.6 6.6l2.2-2.2a1 1 0 0 1 1-.25 11.4 11.4 0 0 0 3.6.57 1 1 0 0 1 1 1V20a1 1 0 0 1-1 1A17 17 0 0 1 3 4a1 1 0 0 1 1-1h3.5a1 1 0 0 1 1 1c0 1.25.2 2.45.57 3.57a1 1 0 0 1-.25 1z"/></svg>

<div class="abs logo-box"><div class="logo-name">CALL ME FOR YOUR PIPES</div></div>

<div class="abs showroom">
  <svg width="14" height="18" viewBox="0 0 14 18"><path fill="var(--blue)" d="M7 0a7 7 0 0 0-7 7c0 5 7 11 7 11s7-6 7-11a7 7 0 0 0-7-7zm0 9.5A2.5 2.5 0 1 1 7 4.5a2.5 2.5 0 0 1 0 5z"/></svg>
  VIEW OUR SHOWROOM
</div>
<div class="abs badge" role="img" aria-label="Australian owned badge"></div>
<div class="abs tagline">It's a great day at<br>Plumbing &amp; Gas service !</div>

<nav class="nav">
  <a style="left:354px">HOME</a>
  <a style="left:430px">ABOUT US</a>
  <a style="left:532px">SERVICES</a>
  <a style="left:630px">GALLERY</a>
  <a style="left:724px">CONTACT US</a>
</nav>

<div class="abs hero" role="img" aria-label="Dark workshop background with plumbing tools"></div>
<div class="abs hero-person" role="img" aria-label="Plumber in hard hat holding a drill"></div>
<h1 class="abs hero-title">CALL ME FOR<br>YOUR PIPES</h1>
<p class="abs hero-text">All of our <span>plumbing and gas services</span> are fully licensed, always on the go with vans that are well stocked for any plumbing situations.</p>
<div class="btn" style="left:111px;top:501px;width:151px;height:45px">GET STARTED <i class="arrow"></i></div>

<div class="abs enquiry"></div>
<div class="abs enquiry-title">FILL THE FORM BELOW &amp; GET QUICK RESPONSE</div>
<div class="field" style="left:111px;width:134px">Name *</div>
<div class="field" style="left:251px;width:134px">Email *</div>
<div class="field" style="left:392px;width:133px">Phone No *</div>
<div class="field" style="left:532px;width:133px">Service *<svg class="abs" style="right:12px;top:19px" width="8" height="5"><path d="M0 0h8L4 5z" fill="#555"/></svg></div>
<div class="btn" style="left:672px;top:777px;width:133px;height:44px;box-shadow:none">SUBMIT NOW</div>
<div class="abs callbox"></div>
<div class="abs callbox-label">CALL US ANYTIME !</div>
<div class="abs callbox-num">0400 555 218</div>
<svg class="abs" style="left:970px;top:790px" width="36" height="36" viewBox="0 0 24 24"><path fill="none" stroke="var(--navy-deep)" stroke-width="1.5" d="M6.6 10.8a15 15 0 0 0 6.6 6.6l2.2-2.2a1 1 0 0 1 1-.25 11.4 11.4 0 0 0 3.6.57 1 1 0 0 1 1 1V20a1 1 0 0 1-1 1A17 17 0 0 1 3 4a1 1 0 0 1 1-1h3.5a1 1 0 0 1 1 1c0 1.25.2 2.45.57 3.57a1 1 0 0 1-.25 1z"/></svg>

<div class="abs splash" role="img" aria-label="Splash of clear blue water"></div>

<div class="feature-icon" style="top:980px"><svg width="30" height="26" viewBox="0 0 30 26"><rect x="2" y="6" width="26" height="16" rx="2" fill="none" stroke="var(--navy)" stroke-width="2"/><path d="M6 2h18" stroke="var(--blue)" stroke-width="2"/></svg></div>
<div class="feature-title" style="top:975px">QUICK RESPONSE</div>
<div class="feature-text" style="top:997px">If you've had enough of tradespeople who never turn up when they say they will.</div>

<div class="feature-icon" style="top:1078px"><svg width="30" height="22" viewBox="0 0 30 22"><rect x="1" y="1" width="28" height="20" rx="2" fill="none" stroke="var(--navy)" stroke-width="2"/><path d="M1 7h28" stroke="var(--blue)" stroke-width="3"/></svg></div>
<div class="feature-title" style="top:1073px">PAYMENT OPTIONS</div>
<div class="feature-text" style="top:1095px">Electronic Transfer, all major cards accepted, Debit Cards and EFTPOS facilities.</div>

<div class="feature-icon" style="top:1176px"><svg width="30" height="26" viewBox="0 0 30 26"><path d="M3 10L15 2l12 8v14H3z" fill="none" stroke="var(--navy)" stroke-width="2"/><rect x="11" y="15" width="8" height="9" fill="var(--blue)"/></svg></div>
<div class="feature-title" style="top:1171px">VIEW OUR SHOWROOM</div>
<div class="feature-text" style="top:1193px">We handle all plumbing and gas installation including domestic and commercial.</div>

<h2 class="abs heading about-title">ABOUT US</h2>
<p class="abs about-text" style="top:1008px">Sam has been in the plumbing and gas industry since high school, his father Ray was a plumber and estimator. Sam has trained with reputable plumbers of his time and achieved apprentice of the year 2 years running, then taking out the "Apprentice of the Year" award for all trades during his apprenticeship.</p>
<p class="abs about-text" style="top:1155px">Originally from Perth, Duncraig, Sam Doyle has been in the plumbing industry for over 30 years. Sam started his apprenticeship at 16, work for many reputable plumbing companies and was a foreman for Keystone Plumbing on commercial sites for many years before starting out on his own in 1998.</p>
<div class="btn" style="left:621px;top:1312px;width:151px;height:47px">READ MORE <i class="arrow"></i></div>

<div class="abs partners"></div>
<div class="partner" style="left:142px;width:155px" role="img" aria-label="Partner badge"></div>
<div class="partner" style="left:360px;width:146px" role="img" aria-label="Partner badge"></div>
<div class="partner" style="left:568px;width:152px" role="img" aria-label="Partner badge"></div>
<div class="partner" style="left:820px;top:1539px;width:72px;height:72px;border-radius:50%" role="img" aria-label="Partner badge"></div>
<div class="partner" style="left:992px;top:1510px;width:66px;height:122px;border-radius:6px" role="img" aria-label="Certification badge"></div>

<h2 class="abs heading section-title" style="top:1750px">OUR SERVICES</h2>

<h3 class="abs heading service-title" style="left:111px;top:1920px">PLUMBING</h3>
<ul class="checklist">
  <li style="left:114px;top:1983px">Domestic &amp; Commercial Installations</li>
  <li style="left:114px;top:2017px">Hot Water System installations, Repair &amp; Maintenance</li>
  <li style="left:114px;top:2052px">Water Purification Systems – under sink filters</li>
  <li style="left:114px;top:2086px">Supply and installation of tank, house and bore pumps</li>
</ul>
<div class="btn" style="left:113px;top:2138px;width:136px;height:43px">VIEW MORE <i class="arrow"></i></div>
<div class="photo" style="left:623px;top:1882px;width:462px;height:345px;background:linear-gradient(135deg,#8a9bb0 0%,#3d5b8f 50%,#2a3c60 100%)" role="img" aria-label="Two plumbers in hard hats reviewing plans"></div>

<div class="photo" style="left:105px;top:2341px;width:472px;height:345px;background:linear-gradient(135deg,#d8dee6 0%,#2e5aa0 45%,#6f8fb5 75%,#c7a64a 100%)" role="img" aria-label="Gas fitter tightening a pipe valve"></div>
<h3 class="abs heading service-title" style="left:681px;top:2380px">GAS SERVICE</h3>
<ul class="checklist">
  <li style="left:684px;top:2442px">All gas pipework installations to kitchen, heaters, BBQ's</li>
  <li style="left:684px;top:2477px">Supply and install gas Hot Water Units</li>
  <li style="left:684px;top:2511px">Leak detection, gas line installation and repairs</li>
  <li style="left:684px;top:2546px">Gas appliance installation</li>
</ul>
<div class="btn" style="left:682px;top:2596px;width:137px;height:45px">VIEW MORE <i class="arrow"></i></div>

<div class="abs provide" role="img" aria-label="Soft grey plumbing background"></div>
<h2 class="abs heading section-title" style="top:2866px">WHAT WE PROVIDE</h2>

<div class="diamond" style="left:194px;top:2987px"></div>
<div class="diamond" style="left:510px;top:2987px"></div>
<div class="diamond" style="left:826px;top:2987px"></div>
<div class="diamond" style="left:356px;top:3127px"></div>
<div class="diamond" style="left:682px;top:3127px"></div>

<svg class="diamond-icon" style="left:252px;top:3040px" viewBox="0 0 44 44"><path d="M4 16h36v24H4z M2 16l6-10h28l6 10" fill="none" stroke="var(--navy)" stroke-width="2"/><rect x="12" y="24" width="8" height="16" fill="var(--blue)"/><rect x="25" y="24" width="9" height="8" fill="none" stroke="var(--navy)" stroke-width="2"/></svg>
<div class="diamond-label" style="left:154px;top:3097px">SHOWROOM</div>

<svg class="diamond-icon" style="left:568px;top:3040px" viewBox="0 0 44 44"><rect x="4" y="4" width="28" height="26" rx="2" fill="none" stroke="var(--navy)" stroke-width="2"/><path d="M9 12h18M9 18h18" stroke="var(--blue)" stroke-width="2"/><circle cx="34" cy="34" r="7" fill="none" stroke="var(--navy)" stroke-width="2"/></svg>
<div class="diamond-label" style="left:470px;top:3097px">SUPPLY &amp; INSTALL</div>

<svg class="diamond-icon" style="left:884px;top:3040px" viewBox="0 0 44 44"><path d="M4 20L22 6l18 14M8 17v21h28V17" fill="none" stroke="var(--navy)" stroke-width="2"/><rect x="17" y="24" width="10" height="8" fill="var(--blue)"/></svg>
<div class="diamond-label" style="left:786px;top:3097px">RENOVATIONS</div>

<svg class="diamond-icon" style="left:414px;top:3180px" viewBox="0 0 44 44"><path d="M10 4v26a8 8 0 0 0 16 0v-6h12" fill="none" stroke="var(--navy)" stroke-width="3"/><path d="M6 4h8M34 20v8" stroke="var(--blue)" stroke-width="3"/></svg>
<div class="diamond-label" style="left:316px;top:3237px">HOT WATER UNITS</div>

<svg class="diamond-icon" style="left:740px;top:3180px" viewBox="0 0 44 44"><rect x="10" y="4" width="20" height="36" rx="2" fill="none" stroke="var(--navy)" stroke-width="2"/><rect x="14" y="9" width="12" height="9" fill="var(--blue)"/><circle cx="20" cy="28" r="4" fill="none" stroke="var(--navy)" stroke-width="2"/></svg>
<div class="diamond-label" style="left:642px;top:3237px">GAS INSTALLATIONS</div>

<h2 class="abs heading section-title" style="top:3500px">PLUMBING &amp; GAS SERVICES</h2>
<p class="abs info-text">Call Me For Your Pipes is a family run business based in Tallowood Vale since 2004, we service Midland to Wannamal, Ellenbrook to Brigadoon, Joondalup and Wanneroo to Bullsbrook, Toodyay to Gingin , Chittering and surrounding areas of Bullsbrook, Brigadoon, Ellenbrook, Averley, Henley Brook, Millendon, Gingin, Bindoon, Wannamal, Chittering, Midland, Upper Swan, Belhus, Wanneroo, Wangara, Malaga and The Vines. All of our plumbing and gas services are fully licensed, always on the go with vans that are well stocked for any plumbing situations. We offer a complete honest and reliable service, no call out fee, free quotes and professional advice. We believe in a duty of care to our customers. At Call Me For Your Pipes no job is too big or too small regardless if it's a complete bathroom, kitchen, laundry make over, new build or renovation. We are suppliers of quality tap ware and fixtures, agents for solar hot water and quality gas systems at an affordable price.</p>
<div class="btn" style="left:534px;top:3852px;width:134px;height:43px">VIEW MORE <i class="arrow"></i></div>

<div class="abs map" role="img" aria-label="Street map showing the business location"></div>
<div class="abs directions">GET DIRECTIONS
  <svg width="16" height="14" viewBox="0 0 16 14"><path d="M10 0l6 5-6 5V7C5 7 2 9 0 14c0-6 3-10 10-10z" fill="#222"/></svg>
</div>
<svg class="abs" style="left:471px;top:4168px" width="24" height="32" viewBox="0 0 14 18"><path fill="#e0332b" d="M7 0a7 7 0 0 0-7 7c0 5 7 11 7 11s7-6 7-11a7 7 0 0 0-7-7z"/><circle cx="7" cy="7" r="2.5" fill="#8a1510"/></svg>
<div class="abs addr"><b>CALL ME FOR YOUR PIPES</b><br>88 Tarrant Street,<br>Tallowood Vale WA 6999</div>

<footer>
  <div class="abs footer"></div>
  <div class="f-icon" style="left:151px;top:4453px"><svg width="18" height="14" viewBox="0 0 18 14"><rect x="1" y="1" width="16" height="12" rx="1" fill="none" stroke="#fff" stroke-width="1.6"/><path d="M1 2l8 6 8-6" fill="none" stroke="#fff" stroke-width="1.6"/></svg></div>
  <div class="f-label" style="left:221px;top:4451px">EMAIL US</div>
  <div class="f-value" style="left:221px;top:4473px">Office@callmeforyourpipes.com.au</div>
  <div class="abs f-logo">CALL ME FOR<br>YOUR PIPES</div>
  <div class="f-icon" style="left:829px;top:4453px"><svg width="18" height="14" viewBox="0 0 18 14"><rect x="1" y="1" width="16" height="12" rx="1" fill="none" stroke="#fff" stroke-width="1.6"/><path d="M1 2l8 6 8-6" fill="none" stroke="#fff" stroke-width="1.6"/></svg></div>
  <div class="f-label" style="left:898px;top:4451px">CONTACT US</div>
  <div class="f-value" style="left:898px;top:4473px">1800 555 019</div>
  <div class="abs f-nav"><span>HOME</span><span class="sep">/</span><span>ABOUT US</span><span class="sep">/</span><span>OUR SERVICES</span><span class="sep">/</span><span>LATEST BLOG</span><span class="sep">/</span><span>REVIEWS</span><span class="sep">/</span><span>TARGETS</span><span class="sep">/</span><span>CONTACT US</span></div>
  <div class="abs f-rule"></div>
  <div class="abs f-copy">© 2020 Call Me For Your Pipes. All Rights Reserved</div>
  <div class="abs f-legal">Privacy Policy &nbsp; / &nbsp; Terms of service</div>
</footer>

</body>
</html>
```